Online Prescription Eyeglass Lens Company Needs a Website

*Update new name to ClearPair. Thx

We are eye doctors with a lab that need a website for a new company based in Southern California called ClearPair. We replace old prescription lenses with new ones next day for most lenses. Patients select the lenses and give us the prescription. We then send a box with a prepaid shipping label. Place the frames in the box and drop them in the mail to our lab. We will custom make new lenses, fit them back into your frames and send them back to you. We would like to compete with www.vizora.com and offer affordable lenses for single vision, bifocal, progressive, sunglass lenses at an affordable price with next day shipping.
Updates

Hi Designers, We have a new name called ClearPair. Can we have the website design reflect the new name and we'll pick our favorites. Thx

Update: The new name is OptiNova . I have not made very many changes or feedback to the submissions because we were bidding for a .com. We won and our new name is OptiNova . This is the last name change.. Please have the website reflect the new name and I'll be providing feedback on the websites . ( I have a separate project for the logo people are working on, so don't worry about creating a logo). Look forward to the submissions. Thanks everyone.

Hi, Just leave the name as ClearPair for now. I will narrow down top designs tonight. Thx

Target Market(s)

Anyone that wears prescription or nonprescription glasses or sunglasses that want next day shipping.

Industry/Entity Type

Eyewear

Number of Pages Required

4 page

Font styles to use
Serif

Colors

Designer to choose colors to be used in the design.

Requirements
Must have
• I need a website that can compete with https://www.vizora.com/.
• We are different from vizora because we can offer same day service or next day shipping.
• It needs to have website that offers the lenses available listed below.
• Needs to be able to upload a prescription and payment feature.
• Pictures of different types of options with small info about each lens option.
• Template Pricing (just use numbers from $79-$179 for now)
• SINGLE VISION LENSES
• HIGH INDEX LENSES
• READING LENSES
• DIGITAL HD PROGRESSIVE LENSES
• RX & NON-RX SUNGLASSES
• RX & NON-RX POLARIZED SUNGLASSES
• COMPUTER LENSES
• TRANSITION LENSES
• BI-FOCAL LENSES

```html
<!DOCTYPE html>
<html lang="en">
<head>
<meta charset="utf-8">
<title>ClearPair – Prescription Lens Replacement</title>
<link rel="stylesheet" href="https://fonts.googleapis.com/css2?family=Poppins:wght@400;500;600;700&family=Open+Sans:wght@400;600;700&display=swap">
<style>
:root{
  --blue:#3a9de2;
  --blue-dark:#2f8ccf;
  --orange:#f7941d;
  --ink:#2b2b2b;
  --text:#6f6f6f;
  --muted:#9a9a9a;
  --light:#f3f3f3;
  --line:#e3e3e3;
  --dark:#262626;
  --footer:#f7f7f7;
  --white:#ffffff;
}
*{box-sizing:border-box;margin:0;padding:0}
html,body{width:1200px;height:2812px;overflow:hidden}
body{font-family:"Open Sans",Arial,sans-serif;color:var(--text);background:var(--white);position:relative}
h1,h2,h3,h4,.logo,.nav a,.btn{font-family:"Poppins",Arial,sans-serif}
a{color:inherit;text-decoration:none}
.btn{display:inline-block;background:var(--orange);color:var(--white);font-weight:600;font-size:11px;letter-spacing:.5px;text-transform:uppercase;padding:8px 16px;border-radius:2px}

/* Header */
.site-header{height:72px;display:flex;align-items:center;padding:0 20px 0 20px;background:var(--white);border-bottom:1px solid var(--line)}
.logo{font-size:26px;font-weight:500;color:var(--ink);letter-spacing:.3px}
.nav{display:flex;gap:26px;margin-left:auto;margin-right:26px}
.nav a{font-size:11px;font-weight:600;color:var(--ink);text-transform:uppercase}
.nav a.active{color:var(--blue)}
.sign-in{font-family:"Poppins",sans-serif;font-size:11px;font-weight:600;color:var(--ink);margin-right:14px;display:flex;align-items:center;gap:5px}

/* Hero */
.hero{position:relative;height:488px;overflow:hidden}
.hero-photo{position:absolute;inset:0;background:linear-gradient(90deg,#d9c7bd 0%,#efe5df 35%,#f6f4f3 65%,#ffffff 100%)}
.hero-copy{position:absolute;left:790px;top:120px;width:340px;text-align:right}
.hero-copy .kicker{font-family:"Poppins",sans-serif;font-size:30px;font-weight:700;color:var(--ink);letter-spacing:2px}
.hero-copy .title{font-family:"Poppins",sans-serif;font-size:104px;font-weight:700;color:var(--blue);line-height:1;margin-top:2px;letter-spacing:3px}
.hero-copy p{font-size:13px;color:var(--ink);margin:14px 0 0 auto;width:240px;text-align:left;line-height:1.5}
.hero-copy .btn{margin-top:22px;margin-right:70px}
.hero-arrows{position:absolute;right:128px;bottom:24px;display:flex;gap:4px}
.hero-arrows span{width:34px;height:34px;background:#b9b9b9;display:flex;align-items:center;justify-content:center}
.scroll-dot{position:absolute;left:582px;top:542px;width:36px;height:36px;border-radius:50%;background:var(--white);border:1px solid var(--line);z-index:2;display:flex;align-items:center;justify-content:center}

/* Join */
.join{height:328px;background:var(--blue);text-align:center;color:var(--white);padding-top:70px}
.join h2{font-size:32px;font-weight:600;letter-spacing:1px}
.join p{font-size:12px;width:640px;margin:14px auto 0;line-height:1.6;color:#e6f2fc}
.join-form{display:flex;width:400px;margin:30px auto 0;height:44px}
.join-form .field{flex:1;background:var(--white);color:var(--muted);font-size:12px;text-align:left;padding:14px 16px}
.join-form .go{width:52px;background:var(--orange);display:flex;align-items:center;justify-content:center}

/* How it works */
.how{height:592px;background:var(--light);padding-top:54px}
.section-title{font-size:32px;font-weight:600;color:var(--ink);text-align:center;letter-spacing:1px}
.title-rule{width:60px;height:2px;background:var(--orange);margin:14px auto 0}
.steps{display:grid;grid-template-columns:repeat(2,460px);gap:50px 100px;justify-content:center;margin-top:60px}
.step{display:flex;align-items:flex-start;gap:32px}
.step-art{width:188px;height:188px;border-radius:50%;flex:none;background:radial-gradient(circle at 50% 45%,#9fd3ef 0%,#4aa7de 70%,#3a8fc6 100%)}
.step-body{padding-top:26px}
.step-no{font-size:11px;font-weight:700;color:var(--orange);text-transform:uppercase}
.step h3{font-size:16px;font-weight:600;color:var(--ink);margin-top:6px;line-height:1.35}
.step p{font-size:11px;line-height:1.6;margin-top:10px;color:var(--text)}

/* Lenses */
.lenses{height:560px;padding-top:68px;position:relative}
.lenses .intro{font-size:12px;text-align:center;width:560px;margin:16px auto 0;line-height:1.6}
.lens-grid{display:grid;grid-template-columns:repeat(4,200px);gap:24px;justify-content:center;margin-top:40px}
.lens-card{border:1px solid var(--line);text-align:center;padding:16px 14px 18px;height:300px}
.lens-card h4{font-size:10px;font-weight:600;color:var(--ink);text-transform:uppercase}
.lens-art{height:96px;margin:12px 0 10px;background:linear-gradient(180deg,#ffffff,#e9eef2);border-radius:4px}
.price{font-family:"Poppins",sans-serif;font-size:24px;font-weight:600;color:var(--blue)}
.stars{display:flex;justify-content:center;gap:2px;margin-top:2px}
.lens-card p{font-size:10px;line-height:1.5;margin:8px 0 12px}
.lens-card .btn{font-size:10px;padding:7px 14px}
.carousel-arrow{position:absolute;top:396px;width:28px;height:28px;border-radius:50%;background:#c9c9c9;display:flex;align-items:center;justify-content:center}
.carousel-arrow.prev{left:100px}
.carousel-arrow.next{right:100px}

/* Testimonial */
.testimonial{height:320px;position:relative;text-align:center;color:var(--white);margin-top:0}
.testimonial-bg{position:absolute;inset:0;background:linear-gradient(90deg,#1c1c1c 0%,#2f2f2f 40%,#3a3a3a 70%,#2a2a2a 100%)}
.testimonial-inner{position:relative;padding-top:56px}
.avatar{width:104px;height:104px;border-radius:50%;background:linear-gradient(180deg,#d8cfc6,#a8998c);border:4px solid var(--white);margin:0 auto}
.t-arrow{position:absolute;top:98px}
.t-arrow.prev{left:428px}
.t-arrow.next{right:428px}
.quote{font-size:13px;font-style:italic;width:700px;margin:22px auto 0;line-height:1.6;color:#e5e5e5}
.author{font-family:"Poppins",sans-serif;font-size:12px;font-weight:600;color:var(--orange);margin-top:12px;text-transform:uppercase}

/* Footer */
.site-footer{height:452px;background:var(--footer);padding:56px 40px 0 40px;position:relative}
.footer-cols{display:grid;grid-template-columns:270px 270px 270px 1fr;}
.footer-cols h4{font-size:13px;font-weight:600;color:var(--ink);text-transform:uppercase}
.footer-cols ul{list-style:none;margin-top:16px}
.footer-cols li{font-size:12px;line-height:2;color:var(--text)}
.news{display:flex;height:38px;margin-top:18px;width:260px}
.news .field{flex:1;background:var(--white);border:1px solid var(--line);font-size:11px;color:var(--muted);padding:11px 12px}
.news .go{width:44px;background:var(--orange);display:flex;align-items:center;justify-content:center}
.follow{margin-top:26px}
.social{display:flex;gap:8px;margin-top:12px}
.social span{width:26px;height:26px;border-radius:50%;background:var(--orange)}
.footer-bottom{position:absolute;left:0;right:0;bottom:0;height:62px;border-top:1px solid var(--line);display:flex;align-items:center;padding:0 40px;font-size:11px}
.cards{margin-left:auto;display:flex;gap:6px}
.cards span{width:36px;height:22px;border-radius:3px;background:#cfd6de}
</style>
</head>
<body>

<header class="site-header">
  <div class="logo">ClearPair</div>
  <nav class="nav">
    <a class="active" href="#">Home</a>
    <a href="#">About us</a>
    <a href="#">Our lenses</a>
    <a href="#">Why ClearPair</a>
    <a href="#">Our process</a>
    <a href="#">Contact us</a>
  </nav>
  <a class="sign-in" href="#"><svg width="11" height="11" viewBox="0 0 12 12"><path d="M2 10l1-3 6-6 2 2-6 6z" fill="#2b2b2b"/></svg>Sign in</a>
  <a class="btn" href="#">Order lenses</a>
</header>

<section class="hero">
  <div class="hero-photo" role="img" aria-label="Close-up photo of a woman wearing black prescription eyeglasses"></div>
  <div class="hero-copy">
    <div class="kicker">EYEGLASS</div>
    <div class="title">LENS</div>
    <p>Adipiscing elit, sed do eiusmod tempor incididunt labore dolore.</p>
    <a class="btn" href="#">Learn more info</a>
  </div>
  <div class="hero-arrows">
    <span><svg width="10" height="10" viewBox="0 0 10 10"><path d="M7 1L3 5l4 4" stroke="#fff" stroke-width="1.6" fill="none"/></svg></span>
    <span><svg width="10" height="10" viewBox="0 0 10 10"><path d="M3 1l4 4-4 4" stroke="#fff" stroke-width="1.6" fill="none"/></svg></span>
  </div>
</section>

<div class="scroll-dot"><svg width="12" height="12" viewBox="0 0 12 12"><path d="M6 1v10M1 6h10" stroke="#3a9de2" stroke-width="2"/></svg></div>

<section class="join">
  <h2>JOIN THE CLEARPAIR</h2>
  <p>Aliquip ex ea commodo consequat. Duis aute irure dolor in reprehenderit in voluptate velit esse cillum dolore eu fugiat nulla pariatur. Excepteur sint occaecat cupidatat non proident, sunt in culpa qui officia deserunt mollit anim id est laborum.</p>
  <div class="join-form">
    <div class="field">Enter email address...</div>
    <div class="go"><svg width="12" height="12" viewBox="0 0 12 12"><path d="M4 1l5 5-5 5" stroke="#fff" stroke-width="2" fill="none"/></svg></div>
  </div>
</section>

<section class="how">
  <h2 class="section-title">HOW IT WORKS</h2>
  <div class="title-rule"></div>
  <div class="steps">
    <div class="step">
      <div class="step-art" role="img" aria-label="Illustration of an optician showing lens options"></div>
      <div class="step-body">
        <div class="step-no">Step 1</div>
        <h3>PICK YOUR LENSES</h3>
        <p>Choose your lens type online and upload your prescription in a few simple steps.</p>
      </div>
    </div>
    <div class="step">
      <div class="step-art" role="img" aria-label="Illustration of a hand placing glasses into a prepaid box"></div>
      <div class="step-body">
        <div class="step-no">Step 2</div>
        <h3>SEND US YOUR<br>FRAMES</h3>
        <p>Place your frames in our prepaid box and drop it in the mail to our lab.</p>
      </div>
    </div>
    <div class="step">
      <div class="step-art" role="img" aria-label="Illustration of a lab technician with an eye chart"></div>
      <div class="step-body">
        <div class="step-no">Step 3</div>
        <h3>WE RE-LENS YOUR<br>GLASSES</h3>
        <p>Our doctors custom make new lenses and fit them back into your own frames.</p>
      </div>
    </div>
    <div class="step">
      <div class="step-art" role="img" aria-label="Illustration of finished glasses on a screen ready to ship"></div>
      <div class="step-body">
        <div class="step-no">Step 4</div>
        <h3>SIGHT, SEALED,<br>DELIVERED</h3>
        <p>Your glasses ship back to you the next day for most lens types we offer.</p>
      </div>
    </div>
  </div>
</section>

<section class="lenses">
  <h2 class="section-title">OUR LENSES</h2>
  <div class="title-rule"></div>
  <p class="intro">Aliquip ex ea commodo consequat. Duis aute irure dolor in reprehenderit in voluptate velit esse cillum dolore eu fugiat nulla pariatur. Excepteur sint.</p>
  <div class="lens-grid">
    <div class="lens-card">
      <h4>Single vision lenses</h4>
      <div class="lens-art" role="img" aria-label="Photo of a pair of clear single vision lenses"></div>
      <div class="price">$79</div>
      <div class="stars"><svg width="60" height="10" viewBox="0 0 60 10"><g fill="#f7941d"><path id="s" d="M5 0l1.5 3.3 3.5.3-2.7 2.3.9 3.5L5 7.5 1.8 9.4l.9-3.5L0 3.6l3.5-.3z"/><use href="#s" x="12"/><use href="#s" x="24"/><use href="#s" x="36"/><use href="#s" x="48"/></g></svg></div>
      <p>Clear everyday lenses cut to your exact prescription.</p>
      <a class="btn" href="#">View more</a>
    </div>
    <div class="lens-card">
      <h4>High index lenses</h4>
      <div class="lens-art" role="img" aria-label="Photo of a row of thin high index lenses"></div>
      <div class="price">$129</div>
      <div class="stars"><svg width="60" height="10" viewBox="0 0 60 10"><g fill="#f7941d"><use href="#s"/><use href="#s" x="12"/><use href="#s" x="24"/><use href="#s" x="36"/><use href="#s" x="48"/></g></svg></div>
      <p>Thinner, lighter lenses for strong prescriptions.</p>
      <a class="btn" href="#">View more</a>
    </div>
    <div class="lens-card">
      <h4>Reading lenses</h4>
      <div class="lens-art" role="img" aria-label="Photo of round black reading glasses"></div>
      <div class="price">$84</div>
      <div class="stars"><svg width="60" height="10" viewBox="0 0 60 10"><g fill="#f7941d"><use href="#s"/><use href="#s" x="12"/><use href="#s" x="24"/><use href="#s" x="36"/><use href="#s" x="48"/></g></svg></div>
      <p>Comfortable close-up vision for books and phones.</p>
      <a class="btn" href="#">View more</a>
    </div>
    <div class="lens-card">
      <h4>Computer lenses</h4>
      <div class="lens-art" role="img" aria-label="Photo of a pair of computer lenses"></div>
      <div class="price">$155</div>
      <div class="stars"><svg width="60" height="10" viewBox="0 0 60 10"><g fill="#f7941d"><use href="#s"/><use href="#s" x="12"/><use href="#s" x="24"/><use href="#s" x="36"/><use href="#s" x="48"/></g></svg></div>
      <p>Reduce eye strain from long hours at the screen.</p>
      <a class="btn" href="#">View more</a>
    </div>
  </div>
  <span class="carousel-arrow prev"><svg width="10" height="10" viewBox="0 0 10 10"><path d="M7 1L3 5l4 4" stroke="#fff" stroke-width="1.6" fill="none"/></svg></span>
  <span class="carousel-arrow next"><svg width="10" height="10" viewBox="0 0 10 10"><path d="M3 1l4 4-4 4" stroke="#fff" stroke-width="1.6" fill="none"/></svg></span>
</section>

<section class="testimonial">
  <div class="testimonial-bg" role="img" aria-label="Dark close-up photo of an eye beside an eye chart"></div>
  <div class="testimonial-inner">
    <div class="avatar" role="img" aria-label="Customer portrait"></div>
    <svg class="t-arrow prev" width="28" height="16" viewBox="0 0 28 16"><path d="M27 8H2M8 1L1 8l7 7" stroke="#fff" stroke-width="2" fill="none"/></svg>
    <svg class="t-arrow next" width="28" height="16" viewBox="0 0 28 16"><path d="M1 8h25M20 1l7 7-7 7" stroke="#fff" stroke-width="2" fill="none"/></svg>
    <p class="quote">“Aliquip ex ea commodo consequat. Duis aute irure dolor in reprehenderit in voluptate velit esse cillum dolore eu fugiat nulla pariatur. Excepteur sint occaecat cupidatat non proident, sunt in culpa qui officia deserunt mollit.”</p>
    <div class="author">Mark Delaney</div>
  </div>
</section>

<footer class="site-footer">
  <div class="footer-cols">
    <div>
      <h4>Navigation</h4>
      <ul><li>Home</li><li>About us</li><li>Our lenses</li><li>Why ClearPair</li><li>Our process</li><li>Contact us</li></ul>
    </div>
    <div>
      <h4>About</h4>
      <ul><li>Why choose us</li><li>Our process</li><li>Our lab</li><li>Make a return</li><li>Blog</li></ul>
    </div>
    <div>
      <h4>Support</h4>
      <ul><li>Track order</li><li>FAQs</li><li>Shipping</li><li>Returns</li><li>Terms</li><li>Privacy</li></ul>
    </div>
    <div>
      <h4>Stay upto date</h4>
      <div class="news">
        <div class="field">Enter email address...</div>
        <div class="go"><svg width="10" height="10" viewBox="0 0 10 10"><path d="M3 1l4 4-4 4" stroke="#fff" stroke-width="2" fill="none"/></svg></div>
      </div>
      <div class="follow">
        <h4>Follow us</h4>
        <div class="social"><span></span><span></span><span></span><span></span></div>
      </div>
    </div>
  </div>
  <div class="footer-bottom">
    <span>Copyright © 2015 ClearPair | All rights reserved</span>
    <div class="cards"><span></span><span></span><span></span><span></span></div>
  </div>
</footer>

</body>
</html>
```